Wealth Advising Business Cards and Stationery
Brightmoor Capital Partners
Wealth Advising Business Cards and Stationery - Financial Services
Creative Brief
Simple
Colin Ashdown
Founder - Managing Director
4419 Hollis Crest Road, Suite 820, Frisco,TX 75036
colin@brightmoorcapitalpartners.example
www.brightmoorcapitalpartners.example
I'd like the logo to be on one side and the contact information on the other.

```html
<!DOCTYPE html>
<html lang="en">
<head>
<meta charset="utf-8">
<title>Brightmoor Capital Partners – Business Card</title>
<link rel="stylesheet" href="https://fonts.googleapis.com/css2?family=Cinzel:wght@500&family=Open+Sans:wght@400;600&display=swap">
<style>
  :root {
    --backdrop: #c9cac8;
    --paper: #ffffff;
    --brand-blue: #1f55a1;
    --ink-grey: #6b6f75;
    --rule: #2a5ea8;
  }
  * { box-sizing: border-box; margin: 0; padding: 0; }
  html, body { width: 1200px; height: 802px; overflow: hidden; }
  body {
    background: var(--backdrop);
    display: flex;
    align-items: center;
    justify-content: center;
    gap: 60px;
    font-family: "Open Sans", Arial, sans-serif;
  }
  .card {
    position: relative;
    width: 520px;
    height: 297px;
    box-shadow: 0 10px 24px rgba(0,0,0,0.22);
  }
  .card--contact { background: var(--paper); }
  .card--brand {
    background: var(--brand-blue);
    display: flex;
    align-items: center;
    justify-content: center;
  }
  .wordmark {
    font-family: "Cinzel", "Times New Roman", serif;
    font-weight: 500;
    text-align: center;
    line-height: 1.1;
    letter-spacing: 0.04em;
  }
  .card--contact .wordmark {
    position: absolute;
    top: 34px;
    right: 40px;
    font-size: 19px;
    color: var(--brand-blue);
  }
  .card--brand .wordmark {
    font-size: 34px;
    color: #ffffff;
  }
  .divider {
    position: absolute;
    top: 100px;
    left: 40px;
    right: 40px;
    height: 1px;
    background: var(--rule);
  }
  .address {
    position: absolute;
    top: 114px;
    right: 40px;
    text-align: right;
    font-size: 10px;
    line-height: 1.5;
    color: var(--ink-grey);
  }
  .marker {
    position: absolute;
    left: 0;
    top: 186px;
    width: 8px;
    height: 30px;
    background: var(--brand-blue);
  }
  .person { position: absolute; left: 40px; top: 182px; }
  .person__name {
    font-family: "Cinzel", "Times New Roman", serif;
    font-size: 16px;
    font-weight: 500;
    color: var(--brand-blue);
    letter-spacing: 0.04em;
  }
  .person__title {
    font-size: 10px;
    color: var(--ink-grey);
    margin-top: 2px;
  }
  .contact-list {
    position: absolute;
    left: 40px;
    top: 226px;
    list-style: none;
    font-size: 9.5px;
    line-height: 1.55;
    color: var(--ink-grey);
  }
  .contact-list .label {
    color: var(--brand-blue);
    font-weight: 600;
    display: inline-block;
    width: 12px;
  }
</style>
</head>
<body>
  <section class="card card--contact" aria-label="Contact side">
    <div class="wordmark">BRIGHTMOOR<br>CAPITAL PARTNERS</div>
    <div class="divider"></div>
    <p class="address">4419 Hollis Crest Road,<br>Suite 820, Frisco,TX 75036</p>
    <span class="marker"></span>
    <div class="person">
      <p class="person__name">COLIN ASHDOWN</p>
      <p class="person__title">Founder - Managing Director</p>
    </div>
    <ul class="contact-list">
      <li><span class="label">t</span>555.014.3826</li>
      <li><span class="label">c</span>555.014.3871</li>
      <li><span class="label">e</span>colin@brightmoorcapitalpartners.example</li>
      <li><span class="label">w</span>www.brightmoorcapitalpartners.example</li>
    </ul>
  </section>

  <section class="card card--brand" aria-label="Brand side">
    <div class="wordmark">BRIGHTMOOR<br>CAPITAL PARTNERS</div>
  </section>
</body>
</html>
```